Communication Skill: NODE Assist

I need a Design for a skill I teach to youth. That's why the title NODE Assist. NODE stands for Thoughts, Emotions, Concerns, Hopes & Desires. Under each word are some examples that are meant to help people discuss certain things. I tried to create something myself but want something much more creative and dynamic. I have attached what I designed because it has the information I need in the design. Want it to have a techie look to it.

```html
<!DOCTYPE html>
<html lang="en">
<head>
<meta charset="utf-8">
<title>NODE Assist – Communication Skill</title>
<link rel="stylesheet" href="https://fonts.googleapis.com/css2?family=Montserrat:wght@800&family=Oswald:wght@600&family=Source+Sans+3:wght@400&display=swap">
<style>
  :root {
    --green-lime: #7ebb00;
    --green-leaf: #5db548;
    --teal: #3db3a1;
    --blue: #21b0e6;
    --hex-rim: #e3e3e3;
    --text-grey: #6b6b6b;
    --line-grey: #c4c4c4;
    --bg-light: #fbfbfb;
    --bg-edge: #e4e4e4;
  }
  html, body {
    margin: 0;
    padding: 0;
    width: 1200px;
    height: 843px;
    overflow: hidden;
  }
  body {
    background: radial-gradient(ellipse at 50% 45%, var(--bg-light) 30%, var(--bg-edge) 100%);
  }
  .poster {
    display: block;
    width: 1200px;
    height: 843px;
  }
  .title-word {
    font-family: "Montserrat", sans-serif;
    font-weight: 800;
    fill: #ffffff;
    font-size: 120px;
    letter-spacing: 4px;
  }
  .subtitle {
    font-family: "Montserrat", sans-serif;
    font-weight: 800;
    fill: var(--green-lime);
    font-size: 74px;
    letter-spacing: 3px;
    text-transform: uppercase;
  }
  .initial {
    font-family: "Oswald", sans-serif;
    font-weight: 600;
    fill: #ffffff;
    font-size: 96px;
  }
  .heading {
    font-family: "Oswald", sans-serif;
    font-weight: 600;
    font-size: 72px;
    letter-spacing: -1px;
  }
  .prompt {
    font-family: "Source Sans 3", sans-serif;
    font-weight: 400;
    font-size: 24px;
    fill: var(--text-grey);
    letter-spacing: 0.5px;
  }
  .prompt-right { text-anchor: end; }
  .dash { fill: none; stroke-width: 2; stroke-dasharray: 8 6; }
  .wire { fill: none; stroke-width: 4; }
  .title-rule { stroke: var(--line-grey); stroke-width: 3; }
</style>
</head>
<body>
<svg class="poster" viewBox="0 0 2000 1405" xmlns="http://www.w3.org/2000/svg">
  <defs>
    <linearGradient id="title-gradient" x1="0" x2="1" y1="0" y2="0">
      <stop offset="0" stop-color="#6cb52d"/>
      <stop offset="0.55" stop-color="#45b68c"/>
      <stop offset="1" stop-color="#22b0e6"/>
    </linearGradient>
    <linearGradient id="arc-gradient" x1="0" x2="1" y1="0" y2="0">
      <stop offset="0" stop-color="#6cb52d"/>
      <stop offset="0.5" stop-color="#3db3a1"/>
      <stop offset="1" stop-color="#21b0e6"/>
    </linearGradient>
    <linearGradient id="figure-gradient" x1="0" x2="0" y1="0" y2="1">
      <stop offset="0" stop-color="#ececec"/>
      <stop offset="0.45" stop-color="#c9dca6"/>
      <stop offset="1" stop-color="#7ebb00"/>
    </linearGradient>
  </defs>

  <!-- Title -->
  <g class="title">
    <line class="title-rule" x1="600" y1="110" x2="770" y2="110"/>
    <line class="title-rule" x1="1250" y1="110" x2="1420" y2="110"/>
    <rect x="770" y="47" width="480" height="123" rx="61.5" fill="url(#title-gradient)"/>
    <text class="title-word" x="1008" y="152" text-anchor="middle">NODE</text>
    <text class="subtitle" x="1016" y="244" text-anchor="middle">Assist</text>
  </g>

  <!-- Dashed connectors -->
  <path class="dash" stroke="var(--green-leaf)" d="M357,472 V600 Q357,632 389,632 H712"/>
  <path class="dash" stroke="var(--green-lime)" d="M137,866 V995 Q137,1025 167,1025 H600"/>
  <path class="dash" stroke="var(--teal)" d="M1622,440 V610 Q1622,640 1592,640 H1250"/>
  <path class="dash" stroke="var(--blue)" d="M1912,790 V962 Q1912,992 1882,992 H1455"/>

  <!-- Wires to the centre -->
  <path class="wire" stroke="url(#arc-gradient)" d="M768,1192 A220,220 0 0 1 1208,1192"/>
  <path class="wire" stroke="var(--green-leaf)" d="M846,830 V938 L903,990"/>
  <path class="wire" stroke="var(--teal)" d="M1130,830 V938 L1072,990"/>
  <path class="wire" stroke="var(--green-lime)" d="M641,1045 V1108 H785"/>
  <path class="wire" stroke="var(--blue)" d="M1335,1060 V1108 H1190"/>
  <path class="dash" stroke="var(--green-leaf)" d="M903,990 L968,1055"/>
  <path class="dash" stroke="var(--teal)" d="M1072,990 L1025,1050"/>
  <path class="dash" stroke="var(--green-lime)" d="M785,1108 H930"/>
  <path class="dash" stroke="var(--blue)" d="M1190,1108 H1050"/>
  <circle cx="903" cy="990" r="9" fill="var(--green-leaf)"/>
  <circle cx="1072" cy="990" r="9" fill="var(--teal)"/>
  <circle cx="785" cy="1108" r="9" fill="var(--green-lime)"/>
  <circle cx="1190" cy="1108" r="9" fill="var(--blue)"/>

  <!-- Hexagons -->
  <g class="hex hex-emotions">
    <polygon fill="var(--hex-rim)" points="846,548 978,624 978,776 846,852 714,776 714,624"/>
    <polygon fill="var(--green-leaf)" points="846,563 965,632 965,768 846,837 727,768 727,632"/>
    <rect role="img" aria-label="Icon of a person with swirling thoughts and a heart" x="768" y="630" width="156" height="130" rx="18" fill="#ffffff" fill-opacity="0.85"/>
  </g>
  <g class="hex hex-concerns">
    <polygon fill="var(--hex-rim)" points="1130,548 1262,624 1262,776 1130,852 998,776 998,624"/>
    <polygon fill="var(--teal)" points="1130,563 1249,632 1249,768 1130,837 1011,768 1011,632"/>
    <rect role="img" aria-label="Icon of a worried person beside a speech bubble with an exclamation mark" x="1058" y="615" width="140" height="160" rx="18" fill="#ffffff" fill-opacity="0.85"/>
  </g>
  <g class="hex hex-thoughts">
    <polygon fill="var(--hex-rim)" points="641,763 773,839 773,991 641,1067 509,991 509,839"/>
    <polygon fill="var(--green-lime)" points="641,778 760,847 760,983 641,1052 522,983 522,847"/>
    <rect role="img" aria-label="Icon of a brain with circuit lines" x="565" y="848" width="152" height="135" rx="18" fill="#ffffff" fill-opacity="0.85"/>
  </g>
  <g class="hex hex-hopes">
    <polygon fill="var(--hex-rim)" points="1335,775 1467,851 1467,1003 1335,1079 1203,1003 1203,851"/>
    <polygon fill="var(--blue)" points="1335,790 1454,859 1454,995 1335,1064 1216,995 1216,859"/>
    <rect role="img" aria-label="Icon of a head profile with a star in a thought bubble" x="1260" y="853" width="168" height="148" rx="18" fill="#ffffff" fill-opacity="0.85"/>
  </g>

  <!-- Central figure area -->
  <ellipse cx="998" cy="1140" rx="85" ry="105" fill="#e9e9e9"/>
  <rect role="img" aria-label="Illustration of a young student in a green shirt" x="830" y="1045" width="305" height="360" rx="60" fill="url(#figure-gradient)"/>

  <!-- Emotions -->
  <g class="section-emotions">
    <circle cx="357" cy="396" r="76" class="dash" stroke="var(--green-leaf)"/>
    <circle cx="357" cy="396" r="57" fill="var(--green-leaf)"/>
    <text class="initial" x="357" y="430" text-anchor="middle">E</text>
    <text class="heading" x="430" y="425" fill="var(--green-leaf)">MOTIONS</text>
    <text class="prompt" y="503"><tspan x="440">I’m…</tspan><tspan x="508">hopeful</tspan><tspan x="616">worried</tspan><tspan x="730">sad</tspan></text>
    <text class="prompt" y="534"><tspan x="440">afraid</tspan><tspan x="553">mad</tspan><tspan x="647">glad</tspan><tspan x="715">happy</tspan></text>
    <text class="prompt" y="565"><tspan x="440">confident</tspan><tspan x="568">insecure</tspan><tspan x="679">lonely</tspan></text>
    <text class="prompt" y="596"><tspan x="440">bothered</tspan><tspan x="553">uncertain</tspan></text>
  </g>

  <!-- Thoughts -->
  <g class="section-thoughts">
    <circle cx="137" cy="790" r="76" class="dash" stroke="var(--green-lime)"/>
    <circle cx="137" cy="790" r="57" fill="var(--green-lime)"/>
    <text class="initial" x="137" y="824" text-anchor="middle">T</text>
    <text class="heading" x="212" y="817" fill="var(--green-lime)">HOUGHTS</text>
    <text class="prompt" y="912"><tspan x="190">It seems…</tspan><tspan x="323">I wonder…</tspan></text>
    <text class="prompt" y="943"><tspan x="190">It’s my opinion…</tspan><tspan x="387">I believe…</tspan></text>
    <text class="prompt" y="974"><tspan x="190">I assume…</tspan><tspan x="323">I think…</tspan></text>
  </g>

  <!-- Concerns -->
  <g class="section-concerns">
    <circle cx="1352" cy="396" r="76" class="dash" stroke="var(--teal)"/>
    <circle cx="1352" cy="396" r="57" fill="var(--teal)"/>
    <text class="initial" x="1352" y="430" text-anchor="middle">C</text>
    <text class="heading" x="1422" y="420" fill="var(--teal)">ONCERNS</text>
    <text class="prompt prompt-right" x="1585" y="510">I worry about…</text>
    <text class="prompt prompt-right" x="1585" y="541">I’m afraid that…</text>
    <text class="prompt prompt-right" x="1585" y="572">I’m nervous because…</text>
    <text class="prompt prompt-right" x="1585" y="603">It bothers me that…</text>
  </g>

  <!-- Hopes -->
  <g class="section-hopes">
    <circle cx="1742" cy="748" r="76" class="dash" stroke="var(--blue)"/>
    <circle cx="1742" cy="748" r="57" fill="var(--blue)"/>
    <text class="initial" x="1742" y="782" text-anchor="middle">H</text>
    <text class="heading" x="1818" y="772" fill="var(--blue)">OPES</text>
    <text class="prompt" y="880"><tspan x="1693">I hope…</tspan><tspan x="1805">I wish…</tspan></text>
    <text class="prompt" y="911"><tspan x="1549">It’s my desire…</tspan><tspan x="1729">I’d like to see…</tspan></text>
    <text class="prompt" y="942"><tspan x="1685">I want…</tspan><tspan x="1801">I need…</tspan></text>
  </g>
</svg>
</body>
</html>
```